Telepsychiatry Healthcare Services

I am a Family Medicine, Psychiatry Mental Health Nurse Practitioner, starting solo practice for mental health care for anxiety, depression, ptsd and adhd. Talk therapy with medication management if applicable. Would like to include my picture.

Target Market(s)

Children, Adolescent and Adults

Industry/Entity Type

Integrative Mental Healthcare

Requirements
Nice to have
• Mental Helath

```html
<!DOCTYPE html>
<html lang="en">
<head>
<meta charset="utf-8">
<title>Telepsychiatry Flyer</title>
<link href="https://fonts.googleapis.com/css2?family=Montserrat:wght@400;500;600;700;800&display=swap" rel="stylesheet">
<style>
  :root {
    --page: #f2f2f2;
    --navy: #0e1538;
    --green: #8fcf7d;
    --green-soft: #93d184;
    --red: #e03a4e;
    --orange: #ee6a45;
    --orange-light: #f4a25a;
    --purple: #6a3a9a;
    --white: #ffffff;
    --photo-light: #ece7df;
    --photo-mid: #d9d3ca;
    --grey-low: #cfd0d6;
  }
  * { margin: 0; padding: 0; box-sizing: border-box; }
  html, body { width: 1200px; height: 1200px; overflow: hidden; background: var(--page); }
  body { font-family: "Montserrat", sans-serif; position: relative; }
  .flyer { position: absolute; left: 217px; top: 63px; width: 767px; height: 1074px; overflow: hidden; }
  .flyer svg.art { position: absolute; inset: 0; }
  .brand { position: absolute; left: 40px; top: 110px; display: flex; align-items: center; gap: 12px; color: var(--white); font-weight: 700; font-size: 22px; line-height: 1.2; }
  .brand-dot { width: 26px; height: 26px; border-radius: 50%; background: var(--green); flex: none; }
  .headline-lead { position: absolute; left: 25px; top: 305px; font-size: 43px; font-weight: 400; color: var(--navy); }
  .headline { position: absolute; left: 24px; top: 370px; font-size: 67px; font-weight: 700; color: var(--navy); letter-spacing: -0.5px; }
  .profile { position: absolute; left: 402px; top: 510px; color: var(--navy); }
  .profile-name { font-size: 40px; font-weight: 800; line-height: 1; }
  .profile-role { margin-top: 18px; font-size: 20px; font-weight: 700; line-height: 30px; }
  .badge { display: inline-block; margin-top: 14px; background: var(--red); color: var(--white); font-size: 20px; font-weight: 700; padding: 3px 8px 4px; border-radius: 17px; }
  .help-title { margin-top: 18px; font-size: 28px; font-weight: 700; }
  .service { position: absolute; left: 402px; width: 340px; height: 87px; background: var(--navy); border-radius: 22px; display: flex; align-items: center; }
  .service-icon { width: 87px; height: 85px; margin-left: 2px; background: var(--green-soft); border-radius: 20px; border: 2px solid var(--navy); flex: none; display: flex; align-items: center; justify-content: center; color: var(--white); }
  .service-text { margin-left: 14px; color: var(--white); font-size: 18.5px; font-weight: 500; line-height: 25px; }
  .service-one { top: 737px; }
  .service-two { top: 842px; }
  .contact { position: absolute; left: 24px; top: 972px; color: var(--white); }
  .contact-title { font-size: 27px; font-weight: 700; }
  .contact-row { display: flex; align-items: center; margin-top: 14px; font-size: 19px; font-weight: 400; }
  .contact-item { display: flex; align-items: center; gap: 10px; }
  .contact-item + .contact-item { margin-left: 62px; }
</style>
</head>
<body>
<div class="flyer">
  <svg class="art" width="767" height="1074" viewBox="0 0 767 1074">
    <defs>
      <linearGradient id="photoTone" x1="0" y1="0" x2="1" y2="1">
        <stop offset="0" stop-color="var(--photo-light)"/>
        <stop offset="1" stop-color="var(--photo-mid)"/>
      </linearGradient>
      <linearGradient id="lowerTone" x1="0" y1="0" x2="0" y2="1">
        <stop offset="0.3" stop-color="var(--white)"/>
        <stop offset="1" stop-color="var(--grey-low)"/>
      </linearGradient>
      <linearGradient id="portraitTone" x1="0" y1="0" x2="0" y2="1">
        <stop offset="0" stop-color="#6b4e40"/>
        <stop offset="0.6" stop-color="#5a4438"/>
        <stop offset="1" stop-color="#22243a"/>
      </linearGradient>
      <linearGradient id="bandTone" x1="0" y1="0" x2="1" y2="0">
        <stop offset="0" stop-color="var(--orange)"/>
        <stop offset="1" stop-color="var(--orange-light)"/>
      </linearGradient>
    </defs>
    <rect class="hero-photo" width="767" height="560" fill="url(#photoTone)" role="img" aria-label="Photo of a patient on a sofa holding a tablet during a video call with a smiling clinician"/>
    <path class="header-accent" d="M0 0 H492 C440 140 260 276 0 278 Z" fill="var(--green)"/>
    <path class="header-panel" d="M0 0 H472 C420 130 250 266 0 270 Z" fill="var(--navy)"/>
    <path class="divider-red" d="M0 512 C200 512 500 462 767 258 V1074 H0 Z" fill="var(--red)"/>
    <path class="lower-panel" d="M0 522 C200 520 500 472 767 272 V1074 H0 Z" fill="url(#lowerTone)"/>
    <rect class="portrait" x="0" y="474" width="401" height="500" rx="28" fill="url(#portraitTone)" opacity="0.85" role="img" aria-label="Portrait photo of the practitioner smiling"/>
    <path class="band-accent" d="M0 970 C200 918 520 928 767 1074 H0 Z" fill="var(--purple)"/>
    <path class="contact-band" d="M0 980 C200 932 470 948 705 1074 H0 Z" fill="url(#bandTone)"/>
  </svg>

  <div class="brand"><span class="brand-dot"></span><span>MindBridge<br>Telepsychiatry</span></div>

  <div class="headline-lead">Need a</div>
  <div class="headline">Psychiatrist?</div>

  <div class="profile">
    <div class="profile-name">Your Name</div>
    <div class="profile-role">Family Medicine, Psychiatry<br>Mental Health Nurse</div>
    <div class="badge">Solo Practitioner</div>
    <div class="help-title">Provide Help With:</div>
  </div>

  <div class="service service-one">
    <div class="service-icon" aria-label="Care icon">
      <svg width="56" height="56" viewBox="0 0 56 56" fill="none" stroke="currentColor" stroke-width="2.4" stroke-linecap="round" stroke-linejoin="round">
        <circle cx="28" cy="20" r="11"/>
        <path d="M28 9v22M22 14c3 2 3 6 0 8M34 14c-3 2-3 6 0 8"/>
        <path d="M6 22v12c0 5 4 8 8 11v6M50 22v12c0 5-4 8-8 11v6"/>
        <path d="M12 30l6 7M44 30l-6 7"/>
      </svg>
    </div>
    <div class="service-text">Mental health care for<br>anxiety, depression,<br>ptsd and adhd</div>
  </div>
  <div class="service service-two">
    <div class="service-icon" aria-label="Talk therapy icon">
      <svg width="56" height="56" viewBox="0 0 56 56" fill="none" stroke="currentColor" stroke-width="2.4" stroke-linecap="round" stroke-linejoin="round">
        <path d="M8 12h30a4 4 0 0 1 4 4v16a4 4 0 0 1-4 4H22l-9 8v-8H8a4 4 0 0 1-4-4V16a4 4 0 0 1 4-4z"/>
        <path d="M15 24h16M23 17v14"/>
        <path d="M47 8v8M43 12h8"/>
      </svg>
    </div>
    <div class="service-text">Talk therapy with<br>medication<br>management</div>
  </div>

  <div class="contact">
    <div class="contact-title">Contact Me For Appointment:</div>
    <div class="contact-row">
      <div class="contact-item">
        <svg width="22" height="22" viewBox="0 0 24 24" fill="none" stroke="currentColor" stroke-width="1.8" stroke-linejoin="round"><path d="M5 3h4l2 5-2.5 1.5a11 11 0 0 0 6 6L16 13l5 2v4a2 2 0 0 1-2 2A17 17 0 0 1 3 5a2 2 0 0 1 2-2z"/></svg>
        <span>123 123 123</span>
      </div>
      <div class="contact-item">
        <svg width="24" height="20" viewBox="0 0 24 20" fill="none" stroke="currentColor" stroke-width="1.6" stroke-linejoin="round"><rect x="2" y="3" width="20" height="14"/><path d="M2 3l10 8 10-8M2 17l7-7M22 17l-7-7"/></svg>
        <span>yourname@email.com</span>
      </div>
    </div>
  </div>
</div>
</body>
</html>
```